Nutrition business needs logo & business card design

We need a business card & logo design for a new company based in Toronto, Ontario Canada called Verdel Wellcraft.

We provide nutrition service using metrics as guide to manage client's progress. Our service creates individualized nutrition and lifestyle strategies that focuses on improving Performance, Longevity and Weight Loss. I would like to see designs that use the color of green, gray, blue and white.

The final design should:

--convey a feeling of connectedness with positive transformation.

-- communicate the idea of awareness with guided effort that yields personal independence for a better and more productive life

Target Market(s)

Professionals who work in the IT/Computer/Engineering/Banking industry specifically Directors, Managers, CEO's.

Industry/Entity Type

Health And Wellness

Contact Information for Business Card

Domric Hale, Owner
email: DHALE@verdelwellcraft.example
tel: - 555-274-9038

Logo Text

better health through analytics or measure to manage

Font styles to use
Other font styles liked:
• Garamound

Colors
ffffff
abd037
85acd3
757575
34a7d7

Requirements
Must have
• Good contrast and decent size font - ease of readability, aesthetically nice colors
Nice to have
• image of chart or graph that conveys measurement or analytics
Should not have
• Borders, images of food,

```html
<!DOCTYPE html>
<html lang="en">
<head>
<meta charset="utf-8">
<title>Verdel Wellcraft — Business Card</title>
<link href="https://fonts.googleapis.com/css2?family=Courier+Prime&family=Lato:wght@400&display=swap" rel="stylesheet">
<style>
  :root {
    --backdrop: #e6e6e6;
    --card: #ffffff;
    --lime: #abd037;
    --slate: #757575;
    --ink-on-lime: #ffffff;
  }
  * { box-sizing: border-box; margin: 0; padding: 0; }
  html, body {
    width: 1200px;
    height: 1023px;
    overflow: hidden;
    background: var(--backdrop);
  }
  .stage {
    width: 1200px;
    height: 1023px;
    display: flex;
    align-items: center;
    justify-content: center;
  }
  .business-card {
    position: relative;
    width: 860px;
    height: 492px;
    background: var(--card);
    box-shadow: 0 2px 6px rgba(0,0,0,0.12);
    overflow: hidden;
  }
  .brand {
    position: absolute;
    left: 50px;
    bottom: 62px;
    display: flex;
    flex-direction: column;
    align-items: flex-start;
  }
  .brand-dot {
    width: 70px;
    height: 70px;
    border-radius: 50%;
    background: var(--lime);
    margin: 0 0 20px 18px;
  }
  .brand-name {
    font-family: "Lato", sans-serif;
    font-weight: 400;
    font-size: 22px;
    letter-spacing: 0.3em;
    color: var(--slate);
    text-transform: uppercase;
    white-space: nowrap;
  }
  .contact-disc {
    position: absolute;
    right: 48px;
    top: 51px;
    width: 390px;
    height: 390px;
    border-radius: 50%;
    background: var(--lime);
    display: flex;
    flex-direction: column;
    justify-content: center;
    padding-left: 54px;
    font-family: "Courier Prime", monospace;
    color: var(--ink-on-lime);
  }
  .person-name {
    font-size: 36px;
    letter-spacing: 0.04em;
    line-height: 1.1;
  }
  .person-role {
    font-size: 19px;
    margin: 6px 0 28px 96px;
  }
  .contact-line {
    font-size: 15.5px;
    line-height: 1.7;
    letter-spacing: 0.02em;
    white-space: nowrap;
  }
</style>
</head>
<body>
  <main class="stage">
    <section class="business-card" aria-label="Verdel Wellcraft business card">
      <div class="brand">
        <span class="brand-dot" aria-hidden="true"></span>
        <span class="brand-name">Verdel Wellcraft</span>
      </div>
      <div class="contact-disc">
        <p class="person-name">Domric Hale</p>
        <p class="person-role">Owner</p>
        <p class="contact-line">DHALE@verdelwellcraft.example</p>
        <p class="contact-line">555-274-9038</p>
      </div>
    </section>
  </main>
</body>
</html>
```